kestrelwind solar flyer design

My company name is Kestrelwind solar, it is a home business that provides consultancy to households to identify their specific power requirements, design pv solar system that meets their needs and get them a minimum of three quotations from three different companies that fit into their budgets.
We do not represent specific product or company but we assist the customer to find the right product for them.
I chose the boomerang because I believe that investing your money in solar just like throwing a boomerang, it will get back to you soon.
I want simple and elegant design that focus on the idea that we have a different approach from other solar companies, our focus on identifying customer's needs rather than trying to sell certain products. So we work for the customer and we are not biased towards any supplier. We will not charge customer anything.
Updated Flyer contents:
Book a free consultation today
Are you keen to have a solar panel system but overwhelmed by sales people telling you what the best is for you?
Call us now and try a different approach.
Our four steps process:
1. Reduce your power demand by increasing your home’s energy efficiency.
2. Design a system that meets your demand.
3. Get you a minimum of three quotations from different suppliers to choose from that will best fit your budget.
4. Installation supervision.
Bonus
With every system installed you will get a free comprehensive 12 months energy saving action plan and quarterly follow up for your property.
Contact details and website address will be given to the final design
Updates
Target Market(s)
target market is middle class families. ages usually between 28-60.
Industry/Entity Type
Business
Look and feel
Each slider illustrates characteristics of the customer's brand and the style your logo design should communicate.

```html
<!DOCTYPE html>
<html lang="en">
<head>
<meta charset="utf-8">
<title>Kestrelwind Solar – Free Consultation Flyer</title>
<link rel="stylesheet" href="https://fonts.googleapis.com/css2?family=Ubuntu:ital,wght@0,300;0,400;0,500;0,700;1,400&display=swap">
<style>
  :root {
    --navy: #0c2d63;
    --navy-deep: #0a2552;
    --sun: #f5c50f;
    --sun-text: #f2c21a;
    --ink: #1b2a48;
    --white: #ffffff;
    --black: #000000;
    --font: "Ubuntu", sans-serif;
  }
  * { margin: 0; padding: 0; box-sizing: border-box; }
  html, body { width: 887px; height: 1200px; overflow: hidden; background: var(--white); }
  .flyer { position: relative; width: 887px; height: 1200px; overflow: hidden; font-family: var(--font); background: var(--black); }

  .masthead { position: absolute; left: 0; top: 0; width: 887px; height: 160px; background: var(--white); }
  .brand { position: absolute; left: 48px; top: 58px; display: flex; align-items: center; gap: 14px; }
  .brand-mark { width: 44px; height: 44px; background: var(--sun); }
  .brand-name { font-weight: 700; font-size: 36px; letter-spacing: 1px; color: var(--navy); text-transform: uppercase; }
  .bulb-art { position: absolute; left: 630px; top: 26px; width: 190px; height: 124px; border-radius: 60px 62px 62px 20px;
    background: radial-gradient(ellipse at 65% 45%, #8fc3ee 0%, #3f7fc0 45%, #1d3f7a 75%, rgba(255,255,255,0) 100%); }

  .hero-art { position: absolute; left: 0; top: 160px; width: 887px; height: 520px;
    background:
      radial-gradient(circle at 430px 180px, rgba(120,190,255,.95) 0%, rgba(40,110,210,.8) 18%, rgba(10,40,90,.4) 34%, rgba(0,0,0,0) 50%),
      radial-gradient(circle at 650px 300px, rgba(255,170,60,.9) 0%, rgba(220,70,30,.4) 8%, rgba(0,0,0,0) 18%),
      radial-gradient(ellipse at 330px 470px, rgba(120,150,190,.6) 0%, rgba(40,60,90,.3) 25%, rgba(0,0,0,0) 45%),
      linear-gradient(180deg, #2a3440 0%, #151b22 55%, #000 100%); }

  .headline { position: absolute; left: 86px; top: 620px; font-weight: 300; font-size: 54px; line-height: 62px; color: var(--white); letter-spacing: -0.5px; }
  .question { position: absolute; left: 87px; top: 785px; width: 360px; font-style: italic; font-size: 22px; line-height: 35px; color: var(--sun-text); }
  .call-out { position: absolute; left: 87px; top: 955px; font-weight: 500; font-size: 18px; color: var(--white); }
  .steps { position: absolute; left: 87px; top: 994px; width: 420px; list-style: none; font-size: 12px; line-height: 16px; letter-spacing: .6px; color: var(--white); }
  .steps li { display: flex; margin-bottom: 4px; }
  .steps .num { width: 24px; flex: none; }

  .bonus { position: absolute; left: 553px; top: 678px; width: 320px; height: 320px; }
  .bonus-title { font-family: var(--font); font-weight: 700; font-size: 24px; letter-spacing: 1.5px; fill: var(--sun); }
  .bonus-copy { font-family: var(--font); font-size: 14.5px; fill: var(--ink); }

  .address { position: absolute; left: 560px; top: 1030px; width: 250px; text-align: center; font-weight: 500; font-size: 16px; line-height: 23px; letter-spacing: 1px; color: var(--white); }

  .footer-band { position: absolute; left: 0; top: 1119px; width: 887px; height: 81px; background: var(--navy-deep); }
  .web { position: absolute; left: 90px; top: 20px; font-weight: 500; font-size: 30px; letter-spacing: 2px; color: var(--white); }
  .contact-icons { position: absolute; left: 610px; top: 18px; display: flex; gap: 7px; }
  .contact-icons svg { width: 42px; height: 42px; }
</style>
</head>
<body>
<div class="flyer">
  <header class="masthead">
    <div class="brand">
      <span class="brand-mark"></span>
      <span class="brand-name">Kestrelwind Solar</span>
    </div>
    <div class="bulb-art" role="img" aria-label="Light bulb containing a sky with solar panels"></div>
  </header>

  <div class="hero-art" role="img" aria-label="Open hand beneath a glowing Earth with a bright sun"></div>

  <h1 class="headline">Book a free<br>consultation today</h1>
  <p class="question">Are you keen to have a solar panel system but overwhelmed by sales people telling you what the best is for you?</p>
  <p class="call-out">Call us now and try a different approach.</p>
  <ol class="steps">
    <li><span class="num">1.</span><span>Reduce your power demand by increasing your home’s energy efficiency.</span></li>
    <li><span class="num">2.</span><span>Design a system that meets your demand.</span></li>
    <li><span class="num">3.</span><span>Get you a minimum of three quotations from different suppliers to choose from that will best fit your budget.</span></li>
    <li><span class="num">4.</span><span>Installation supervision.</span></li>
  </ol>

  <svg class="bonus" viewBox="0 0 320 320" aria-label="Bonus offer">
    <defs>
      <clipPath id="bonus-top"><rect x="0" y="0" width="320" height="115"/></clipPath>
    </defs>
    <g transform="rotate(17 160 160)">
      <g fill="var(--white)">
        <rect x="55" y="55" width="210" height="210"/>
        <rect x="55" y="55" width="210" height="210" transform="rotate(15 160 160)"/>
        <rect x="55" y="55" width="210" height="210" transform="rotate(30 160 160)"/>
        <rect x="55" y="55" width="210" height="210" transform="rotate(45 160 160)"/>
        <rect x="55" y="55" width="210" height="210" transform="rotate(60 160 160)"/>
        <rect x="55" y="55" width="210" height="210" transform="rotate(75 160 160)"/>
      </g>
      <g fill="var(--sun)">
        <rect x="62" y="62" width="196" height="196"/>
        <rect x="62" y="62" width="196" height="196" transform="rotate(15 160 160)"/>
        <rect x="62" y="62" width="196" height="196" transform="rotate(30 160 160)"/>
        <rect x="62" y="62" width="196" height="196" transform="rotate(45 160 160)"/>
        <rect x="62" y="62" width="196" height="196" transform="rotate(60 160 160)"/>
        <rect x="62" y="62" width="196" height="196" transform="rotate(75 160 160)"/>
      </g>
      <g fill="var(--navy)" clip-path="url(#bonus-top)">
        <rect x="62" y="62" width="196" height="196"/>
        <rect x="62" y="62" width="196" height="196" transform="rotate(15 160 160)"/>
        <rect x="62" y="62" width="196" height="196" transform="rotate(30 160 160)"/>
        <rect x="62" y="62" width="196" height="196" transform="rotate(45 160 160)"/>
        <rect x="62" y="62" width="196" height="196" transform="rotate(60 160 160)"/>
        <rect x="62" y="62" width="196" height="196" transform="rotate(75 160 160)"/>
      </g>
      <text class="bonus-title" x="160" y="98" text-anchor="middle">BONUS</text>
      <text class="bonus-copy" text-anchor="middle">
        <tspan x="160" y="137">With every system installed</tspan>
        <tspan x="160" y="156">you will get a free</tspan>
        <tspan x="160" y="175">comprehensive 12 months</tspan>
        <tspan x="160" y="194">energy saving action plan and</tspan>
        <tspan x="160" y="213">quarterly follow up for your</tspan>
        <tspan x="160" y="232">property</tspan>
      </text>
    </g>
  </svg>

  <address class="address" style="font-style:normal">4470 Juniper Ridge Lane<br>Brookfield, Idaho 83611<br>208-555-0147</address>

  <footer class="footer-band">
    <div class="web">www.kestrelwindsolar.net</div>
    <div class="contact-icons">
      <svg viewBox="0 0 42 42" aria-label="Home"><circle cx="21" cy="21" r="21" fill="var(--sun)"/><path d="M10 22 L21 12 L32 22 M14 20 V31 H19 V25 H23 V31 H28 V20" fill="none" stroke="var(--white)" stroke-width="2.6" stroke-linejoin="round"/></svg>
      <svg viewBox="0 0 42 42" aria-label="Phone"><circle cx="21" cy="21" r="21" fill="var(--sun)"/><path d="M16 11 h4 l1 6 -3 2 c1 3 3 5 5 6 l2 -3 6 1 v4 c0 2 -1 3 -3 3 C18 30 12 24 12 14 c0-2 1-3 4-3z" fill="var(--white)"/></svg>
      <svg viewBox="0 0 42 42" aria-label="Email"><circle cx="21" cy="21" r="21" fill="var(--sun)"/><rect x="10" y="13" width="22" height="16" fill="none" stroke="var(--white)" stroke-width="2.4"/><path d="M10 13 L21 22 L32 13" fill="none" stroke="var(--white)" stroke-width="2.4"/></svg>
    </div>
  </footer>
</div>
</body>
</html>
```